Criação de Folder para Tecnologia & Ciencias
A empresa queria:
" A Quitafor é uma empresa que desenvolve e fornece o sistema de cobrança Quitafor para empresas de cobrança (escritórios de cobrança, assessorias de cobranças, escritórios de advogados), tais clientes chamamos de ASSESSORIAS, e também fornecemos o sistema para empresas que possuem uma grande quantidade de clientes inadimplentes e que fazem a cobrança destes clientes internamente através de um departamento de cobrança, estes clientes chamamos de CREDORES. Alguns clientes ASSESSORIAS: www.grupoltv.com.br www.dornelesmota.com.br www.rixamonte.com.br Alguns clientes CREDORES: www.brightlane.com www.grupovelarim.com.br www.tadeus.com.br Todos os produtos e serviços que comercializamos são através da plataforma Quitafor, por exemplo, para que um cliente utilize nosso produto “Painel de Acordos” ele precisa contratar o Quitafor já que suas configurações são através do sistema, da mesma forma o serviço de “SMS”, já que as campanhas são criadas e disparadas pelo sistema Quitafor. O sistema Quitafor “nasceu” primeiro que a empresa Quitafor, já que dois dos atuais sócios possuíram uma empresa anterior de 2012 até a abertura da Quitafor em 1 de setembro de 2015. Esta empresa desenvolvia um sistema focado para assessorias de cobrança, porém em uma tecnologia antiga, e então resolveram criar um novo software com tecnologias atuais na época e para isto buscaram um investidor e juntos optaram por criar uma nova empresa, uma nova marca. Nossa logo foi construída através da plataforma Marca Pronta e gostamos muito do resultado! E estamos aqui novamente buscando que seus profissionais nos ajudem a criar novos materiais que hoje se fazem necessários para nós. "

```html
<!DOCTYPE html>
<html lang="pt-BR">
<head>
<meta charset="utf-8">
<title>Folder Quitafor – Plataforma de Cobrança</title>
<link href="https://fonts.googleapis.com/css2?family=Montserrat:wght@600;700;800&family=Open+Sans:wght@400;600;700&display=swap" rel="stylesheet">
<style>
:root{
  --bg:#eceef2;
  --paper:#ffffff;
  --navy:#1b2f6b;
  --blue:#2b4fa6;
  --blue-light:#3f6cc9;
  --text:#4a5260;
  --muted:#8a93a0;
  --green:#43a34a;
  --orange:#ee8a22;
  --gray-box:#c9ced6;
}
*{box-sizing:border-box;margin:0;padding:0}
html,body{width:1200px;height:1200px;overflow:hidden;background:var(--bg)}
body{font-family:"Open Sans",Arial,sans-serif;color:var(--text);position:relative}
.spread{position:absolute;left:30px;top:380px;width:1140px;height:440px;background:var(--paper);box-shadow:0 6px 24px rgba(20,30,60,.18);overflow:hidden}
.panel{position:absolute;top:0;height:100%}
.fold{position:absolute;top:0;width:1px;height:100%;background:rgba(0,0,0,.06)}
h2.panel-title{font-family:"Montserrat",Arial,sans-serif;font-weight:700;color:var(--blue);font-size:13px;margin-bottom:10px}
p{font-size:6.6px;line-height:1.55;margin-bottom:7px;text-align:justify}
.sub{font-family:"Montserrat",Arial,sans-serif;font-weight:700;color:var(--blue);font-size:6.6px;margin:6px 0 3px;letter-spacing:.3px}

/* panel 1 */
.intro{left:0;width:200px;padding:24px 18px}
.intro .illustration{position:absolute;left:18px;right:18px;bottom:22px;height:70px;background:linear-gradient(135deg,#e6eefb,#b9cdf0);border-radius:4px}

/* panel 2 */
.solution{left:200px;width:320px}
.solution .edge{position:absolute;left:0;top:0;width:14px;height:100%;background:var(--blue)}
.solution .portrait{position:absolute;left:14px;top:0;width:96px;height:100%;background:linear-gradient(180deg,#dfe3ea,#b8bfca 60%,#8d96a4)}
.solution .headline{position:absolute;left:110px;top:0;width:210px;height:88px;background:var(--navy);padding:16px 14px}
.solution .headline p{color:#fff;font-size:7.2px;font-weight:600;text-align:left;line-height:1.5}
.solution .flow{position:absolute;left:116px;top:100px;width:200px;height:240px}
.brand{position:absolute;left:110px;width:210px;bottom:34px;text-align:center;font-family:"Montserrat",Arial,sans-serif;font-weight:700;font-size:22px;color:var(--navy)}

/* panel 3 */
.benefits{left:520px;width:300px}
.benefits .workspace{height:96px;background:linear-gradient(180deg,#f3f5f8,#c8d0dc)}
.benefits .content{padding:14px 20px}
.benefits h2{font-family:"Montserrat",Arial,sans-serif;font-weight:800;color:var(--navy);font-size:10px;margin-bottom:8px}

/* panel 4 */
.modules{left:820px;width:320px}
.modules .content{position:absolute;left:0;top:0;width:184px;padding:24px 16px}
.tile{height:44px;background:linear-gradient(135deg,var(--navy),var(--blue-light));border-radius:2px;margin:6px 0}
.modules .team{position:absolute;left:184px;top:0;width:136px;height:100%;background:linear-gradient(180deg,#cfd6e0,#8e9aab);}
.modules .team-band{position:absolute;left:184px;top:0;width:40px;height:100%;background:var(--blue);clip-path:polygon(0 0,100% 0,30% 100%,0 100%)}
</style>
</head>
<body>
<div class="spread">

  <section class="panel intro">
    <h2 class="panel-title">Plataforma de Cobrança</h2>
    <p>O Quitafor é uma plataforma completa de cobrança, criada para assessorias e credores que buscam mais controle, agilidade e resultado em cada etapa da recuperação de crédito.</p>
    <p>Com tecnologia atual e acesso pela web, a equipe trabalha de qualquer lugar com segurança, integrando carteiras, campanhas e acordos em um único ambiente.</p>
    <p>Desde 2015 evoluímos junto com nossos clientes, unindo experiência de mercado e inovação contínua para simplificar a rotina de cobrança.</p>
    <div class="illustration" role="img" aria-label="Ilustração de nuvem com ícones de tecnologia"></div>
  </section>
  <div class="fold" style="left:200px"></div>

  <section class="panel solution">
    <div class="edge"></div>
    <div class="portrait" role="img" aria-label="Foto de atendente com headset"></div>
    <div class="headline"><p>Reunimos em plataforma única toda a experiência dos nossos profissionais, em gestão, tecnologia e desenvolvimento, para oferecer o Quitafor: o melhor sistema de cobrança do mercado.</p></div>
    <svg class="flow" viewBox="0 0 200 240" font-family="Open Sans, sans-serif" font-size="5.5">
      <g fill="#4a5260" font-weight="700" text-anchor="middle">
        <text x="20" y="8">Integração</text><text x="60" y="8">Carteiras</text><text x="100" y="8">Estratégia</text><text x="140" y="8">Canais</text><text x="180" y="8">Resultados</text>
      </g>
      <g stroke="#9aa3ad" stroke-width=".8" fill="none">
        <path d="M38 60H44M38 100H44M38 140H44M38 180H44M44 60V180M44 120H48"/>
        <path d="M72 120H84M76 80V160M76 80H84M76 160H84"/>
        <path d="M116 80H124M116 120H124M116 160H124"/>
        <path d="M156 120H162M162 36V216"/>
      </g>
      <g fill="var(--gray-box)"><rect x="2" y="52" width="36" height="16" rx="2"/><rect x="2" y="92" width="36" height="16" rx="2"/><rect x="2" y="132" width="36" height="16" rx="2"/><rect x="2" y="172" width="36" height="16" rx="2"/></g>
      <g fill="var(--navy)"><rect x="48" y="100" width="24" height="40" rx="2"/><rect x="84" y="72" width="32" height="16" rx="2"/><rect x="84" y="112" width="32" height="16" rx="2"/><rect x="84" y="152" width="32" height="16" rx="2"/></g>
      <g fill="var(--green)"><rect x="124" y="52" width="32" height="16" rx="2"/><rect x="124" y="72" width="32" height="16" rx="2"/><rect x="124" y="112" width="32" height="16" rx="2"/><rect x="124" y="152" width="32" height="16" rx="2"/></g>
      <g fill="var(--orange)"><rect x="166" y="30" width="32" height="14" rx="2"/><rect x="166" y="62" width="32" height="14" rx="2"/><rect x="166" y="94" width="32" height="14" rx="2"/><rect x="166" y="126" width="32" height="14" rx="2"/><rect x="166" y="158" width="32" height="14" rx="2"/><rect x="166" y="190" width="32" height="14" rx="2"/></g>
      <g fill="#2c3440" text-anchor="middle"><text x="20" y="62">Arquivos</text><text x="20" y="102">API</text><text x="20" y="142">Bureau</text><text x="20" y="182">Portal</text></g>
      <g fill="#fff" text-anchor="middle">
        <text x="60" y="122">Regras</text><text x="100" y="82">Filas</text><text x="100" y="122">Score</text><text x="100" y="162">Regras</text>
        <text x="140" y="62">Discador</text><text x="140" y="82">SMS</text><text x="140" y="122">E-mail</text><text x="140" y="162">URA</text>
        <text x="182" y="39">Acordos</text><text x="182" y="71">Boletos</text><text x="182" y="103">Pix</text><text x="182" y="135">Baixas</text><text x="182" y="167">Painéis</text><text x="182" y="199">BI</text>
      </g>
    </svg>
    <div class="brand">Quitafor</div>
  </section>
  <div class="fold" style="left:520px"></div>

  <section class="panel benefits">
    <div class="workspace" role="img" aria-label="Foto de mesa de trabalho com monitores"></div>
    <div class="content">
      <h2>OS PRINCIPAIS BENEFÍCIOS DA PLATAFORMA</h2>
      <div class="sub">MAIS CONTROLE DA OPERAÇÃO</div>
      <p>Acompanhe carteiras, equipes e metas em tempo real, com indicadores claros para decidir rápido.</p>
      <div class="sub">MAIS PRODUTIVIDADE</div>
      <p>Automatize tarefas repetitivas e concentre a equipe nas negociações que trazem retorno.</p>
      <div class="sub">MAIS RECUPERAÇÃO</div>
      <p>Campanhas por SMS, e-mail e discador disparadas pelo próprio sistema ampliam o contato com cada devedor.</p>
      <div class="sub">MAIS SEGURANÇA</div>
      <p>Dados protegidos, acesso por perfil e histórico completo de cada ação registrada na plataforma.</p>
    </div>
  </section>
  <div class="fold" style="left:820px"></div>

  <section class="panel modules">
    <div class="content">
      <h2 class="panel-title">Módulos de Cobrança</h2>
      <p>Cada módulo foi pensado para uma etapa da cobrança e pode ser contratado conforme a necessidade da operação.</p>
      <div class="tile" role="img" aria-label="Imagem do módulo Painel de Acordos"></div>
      <div class="sub">PAINEL DE ACORDOS</div>
      <p>O devedor negocia on-line, com regras definidas pelo credor.</p>
      <div class="tile" role="img" aria-label="Imagem do módulo de campanhas SMS"></div>
      <div class="sub">CAMPANHAS DE SMS</div>
      <p>Crie e dispare mensagens direto do Quitafor.</p>
      <p>O Quitafor se adapta ao tamanho da sua empresa, do pequeno escritório ao grande credor.</p>
    </div>
    <div class="team" role="img" aria-label="Foto de profissionais em reunião"></div>
    <div class="team-band"></div>
  </section>

</div>
</body>
</html>
```